Software Product Brochure

tavrel is a new cloud based hotel management platform, this solution is our new offering to the hospitality vertical.The solution being cloud based, it is scalable, serving everyone from small Inns, bread & breakfast, hotels, service apartments and resorts to branded-chain operators. Our software is self configurable by hotel based on type of business and spans both guest facing and back office functions.

Hospitality Solution that enables Operational Excellence and widens Customer Reach

BELOW IS A SIMPLE BRIEF ON SOLUTION BUT ACTUAL CONTENT TO BE USED IN DESIGN AND BROCHURE MUST BE FROM THE ENCLOSED DOCUMENTS WITH THIS PROJECT.

A truly Integrated Solution
Manages Distributed Operational Work-flows
Inventory Distributions, Sales and Marketing
Strategic Planning /Reporting and Management

No Compromise, Cloud based solution – at affordable cost, low learning curve, requiring minimal Infrastructure

PMS at an affordable price

Easy to adapt and Simple to use, One platform can serve all of the brands within a chain

Same UI across all brands reduces training efforts

No Servers required, No Installation and Zero maintenance

Online wizard based Installation , reduces cost of setup & training.

Channel Manager- Centralized rates and Real Time inventory distribution

Travel Agents & Corporate logins with specific rates

Unlimited package & rates creations with date validations

Short Learning Curve, Improved Revenues & ROI

Data Security with 99.5% server uptime and Offline Report Availability

Anywhere anytime benefit

Tavrel helps by offering a more cost-effective alternative to on-premises applications. The major benefit that it offers is zero capital expense, lower cost of ownership, faster implementation, quicker training, and a quick return-on-investment are just some of the paybacks. Hotels only need to subscribe to the bandwidth through a reliable Internet ISP

The market is a mature market with many competitors. A few very well established with some good track record. This brochure is targeted at the global market. The target market is jaded with the number of options available. We will focus on small and mid size hotels with a hope that the product would excite them as the competitors offer very basic and more expensive solution whereas we offer a more feature rich and a growing platform.

We are hoping that the brochure will stand-out from the crowd and will compel the market to browse through what we do.

Some key competitors include -
http://www.lodgivo.example
http://www.bedvantix.example
http://www.quorralobby.example
http://www.stayplexa.example

We have a company and sample product brochure we made (both attached). We have also developed a web site (see www.tavrelstays.example). The brochure design need not conform to the web site, if (and only if) you can come up with a really attention seeking design (we could consider redesign of the web site).

The content of the brochure will largely conform to the sample brochure submitted because we have carefully taken the content out for the sample brochure.

——————
We also want below quote to be enclosed and highlighted some place in brochure in both versions

QUOTE START.....

"We travel a lot and want to be able to see how the occupancy is at anytime. We wanted a technology which could connect our HO to property and also help us manage multiple properties.

With tavrel adoption not only have we streamlined our operations but also seen a 20% jump in occupancy

Qorvin –MD,
Q-Hospitality

QUOTE END
——————
Updates

I have a website www.tavrelstays.example. The theme and colour scheme of brochure must match this and both brochure designs should be slightly different. One is full spec brochure and other is a summary of same.

Target Market(s)

This is meant for hotels

Industry/Entity Type

Hospitality

Requirements
Must have
• Colour theme must match www.tavrelstays.example
Nice to have
• The design should be elegant and professional in appearance but playful and not very serious.
Should not have
• Weird colours or images with colours which do not go with my website theme.

```html
<!DOCTYPE html>
<html lang="en">
<head>
<meta charset="utf-8">
<title>Tavrel – Cloud Hotel Management Brochure</title>
<link href="https://fonts.googleapis.com/css2?family=Open+Sans:wght@300;400;600;700&display=swap" rel="stylesheet">
<style>
  :root {
    --brand-red: #c8220f;
    --text-grey: #5a5a5a;
    --email-grey: #5f5f5f;
    --white: #ffffff;
    --photo-dark: #5b5450;
    --photo-mid: #8d8580;
    --photo-light: #c9c4bf;
    --device-dark: #3a3d42;
    --device-light: #d9dcdf;
  }
  html, body {
    margin: 0;
    padding: 0;
    overflow: hidden;
    background: var(--white);
  }
  .brochure {
    position: relative;
    width: 849px;
    height: 1200px;
    overflow: hidden;
    background: var(--white);
    font-family: "Open Sans", Arial, sans-serif;
  }
  .hero-photo {
    position: absolute;
    left: 0;
    top: 0;
    width: 849px;
    height: 500px;
    background:
      linear-gradient(to bottom, rgba(255,255,255,0) 0%, rgba(255,255,255,0) 62%, rgba(255,255,255,0.85) 88%, var(--white) 100%),
      radial-gradient(ellipse at 60% 55%, var(--photo-light) 0%, var(--photo-mid) 45%, var(--photo-dark) 100%);
  }
  .intro {
    position: absolute;
    left: 48px;
    top: 488px;
    width: 340px;
    color: var(--text-grey);
    font-weight: 400;
    font-size: 16.4px;
    line-height: 19.5px;
  }
  .intro p {
    margin: 0 0 19.5px;
  }
  .devices-photo {
    position: absolute;
    left: 50px;
    top: 958px;
    width: 384px;
    height: 208px;
    background: linear-gradient(135deg, var(--device-dark) 0%, #6f7880 45%, var(--device-light) 100%);
    border-radius: 4px;
  }
  .contact-email {
    position: absolute;
    left: 50px;
    top: 1164px;
    width: 375px;
    text-align: center;
    font-weight: 700;
    font-size: 16px;
    color: var(--email-grey);
  }
  .benefits-panel {
    position: absolute;
    left: 425px;
    top: 446px;
    width: 376px;
    height: 754px;
    background: var(--brand-red);
  }
  .benefits-list {
    list-style: none;
    margin: 0;
    padding: 50px 20px 0 27px;
    color: var(--white);
    font-size: 16.4px;
    line-height: 19px;
  }
  .benefits-list li {
    margin: 0 0 18px;
  }
</style>
</head>
<body>
  <main class="brochure">
    <div class="hero-photo" role="img" aria-label="Restaurant table with glasses, plates and a tablet showing the Tavrel hotel management dashboard"></div>

    <section class="intro">
      <p>Tavrel helps by offering a more cost-effective alternative to on-premises applications. The major benefit that it offers is zero capital expense, lower cost of ownership, faster implementation, quicker training, and a quick return-on-investment are just some of the paybacks. Hotels only need to subscribe to the bandwidth through a reliable Internet ISP.</p>
      <p>The market is a mature market with many competitors. A few very well established with some good track record. This brochure is targeted at the global market. The target market is jaded with the number of options available. We will focus on small and mid size hotels with a hope that the product would excite them as the competitors offer very basic and more expensive solution whereas we offer a more feature rich and a growing platform.</p>
    </section>

    <div class="devices-photo" role="img" aria-label="Desktop monitor and tablet displaying the Tavrel reservation chart and point of sale screens"></div>
    <div class="contact-email">sales@tavrelstays.example</div>

    <aside class="benefits-panel">
      <ul class="benefits-list">
        <li>No Compromise, Cloud based solution – at affordable cost, low learning curve, requiring minimal Infrastructure</li>
        <li>PMS at an affordable price</li>
        <li>Easy to adapt and Simple to use,<br>One platform can serve all of the brands within a chain</li>
        <li>Same UI across all brands reduces training efforts</li>
        <li>No Servers required, No Installation and Zero maintenance</li>
        <li>Online wizard based Installation, reduces cost of setup &amp; training</li>
        <li>Channel Manager- Centralized rates and Real Time inventory distribution</li>
        <li>Travel Agents &amp; Corporate logins with specific rates</li>
        <li>Unlimited package &amp; rates creations with date validations</li>
        <li>Short Learning Curve, Improved Revenues &amp; ROI</li>
        <li>Data Security with 99.5% server uptime and Offline Report Availability</li>
        <li>Anywhere anytime benefit</li>
      </ul>
    </aside>
  </main>
</body>
</html>
```